Corporate Template

Looking for a set of corporate slides to be made which contain multiple different slides and orientations. Looking for at least 8 to 10 different master pages plus a Coversheet and closeout page. Incorporating a color palate similar to our logo coloring is preferred.
I have attached a logo.
I like the clever pixel yard designs best so far. They seem to fit what I'm looking for in terms of visual appearance.
Reason: I'm trying to allow time for a couple new designers to incorporate some changes I requested to their existing designs.

```html
<!DOCTYPE html>
<html lang="en">
<head>
<meta charset="utf-8">
<title>Sample Design 5 – Corporate Slide Masters</title>
<link href="https://fonts.googleapis.com/css2?family=Arimo:wght@400;700&display=swap" rel="stylesheet">
<style>
:root{
  --brand:#2f5c9f;
  --brand-dark:#0d2e66;
  --brand-mid:#6a9ad0;
  --brand-light:#a9ccf2;
  --brand-bright:#1a7ac4;
  --ink:#333;
  --muted:#999;
  --row-a:#d9d9d9;
  --row-b:#eeeeee;
  --white:#fff;
}
*{box-sizing:border-box;margin:0;padding:0}
html,body{width:1200px;height:1000px;overflow:hidden;background:var(--white);font-family:"Arimo",Arial,sans-serif}
.canvas{position:relative;width:1200px;height:1000px}
.sheet-title{position:absolute;top:56px;left:0;width:100%;text-align:center;font-size:28px;color:var(--brand);font-weight:400}
.slide{position:absolute;width:332px;height:254px;background:var(--white);overflow:hidden}
.slide--wide{width:338px}
.slide-title{position:absolute;left:33px;top:16px;font-size:13px;font-weight:700;color:var(--brand)}
.emblem{position:absolute;left:4px;top:2px;width:24px;height:22px;border-radius:50%;background:radial-gradient(circle,var(--brand-mid) 0%,var(--brand) 60%,var(--white) 72%)}
.footer-band{position:absolute;left:0;bottom:0;width:100%;height:20px;background:var(--brand)}
.footer-name{position:absolute;right:6px;top:4px;color:var(--white);font-size:6px;line-height:6px;text-align:center;font-weight:400}
.footer-name b{font-weight:400;display:block;font-size:4px;line-height:5px}
/* cover & close */
.hero-band{position:absolute;left:0;top:0;width:100%;height:100px;background:radial-gradient(ellipse at 50% 100%,#1a7fd0 0%,var(--brand) 55%,#2a55a0 100%)}
.cover-title{position:absolute;top:123px;width:100%;text-align:center;font-size:15px;color:var(--brand)}
.cover-date{position:absolute;top:148px;width:100%;text-align:center;font-size:7px;color:var(--muted)}
.rule{position:absolute;left:0;width:100%;height:3px;background:var(--brand)}
.brand-band{position:absolute;left:0;top:175px;width:100%;height:79px;background:var(--brand)}
.brand-name{position:absolute;top:14px;width:100%;text-align:center;color:var(--white);font-size:22px;font-weight:400;letter-spacing:1px;line-height:24px}
.brand-name span{display:block;font-size:9px;line-height:12px;letter-spacing:0}
/* content */
.bullets{position:absolute;left:34px;top:50px;font-size:8.5px;color:var(--ink);line-height:12px;list-style:none}
.bullets li:before{content:"";display:inline-block;width:4px;height:4px;border-radius:50%;background:var(--brand);margin-right:5px;vertical-align:middle}
.bullets .l2{padding-left:18px}.bullets .l3{padding-left:30px}.bullets .l4{padding-left:44px}.bullets .l5{padding-left:58px}
.bullets .l2:before,.bullets .l3:before,.bullets .l4:before,.bullets .l5:before{width:4px;height:1px;border-radius:0;background:var(--ink)}
.chart{position:absolute;left:0;top:0;width:100%;height:100%}
.chart text{font-family:"Arimo",Arial,sans-serif;fill:var(--ink)}
.data-table{position:absolute;left:16px;top:64px;width:297px;border-collapse:collapse;font-size:5.5px;color:var(--ink)}
.data-table th{background:var(--brand);color:var(--white);height:14px;font-weight:700}
.data-table th:first-child{text-align:left;padding-left:4px}
.data-table td{height:14.5px;text-align:center;border-right:1px solid var(--white)}
.data-table td:first-child{text-align:left;padding-left:4px}
.data-table tr:nth-child(odd) td{background:var(--row-a)}
.data-table tr:nth-child(even) td{background:var(--row-b)}
.blank-label{position:absolute;top:116px;width:100%;text-align:center;font-size:7px;font-weight:700;color:var(--brand)}
</style>
</head>
<body>
<div class="canvas">
  <h1 class="sheet-title">Sample Design 5</h1>

  <!-- Cover -->
  <section class="slide" style="left:25px;top:148px">
    <div class="hero-band" role="img" aria-label="Banner with rows of light blue dots on a blue gradient"></div>
    <h2 class="cover-title">Presentation Template</h2>
    <p class="cover-date">October 26, 2013</p>
    <div class="rule" style="top:168px"></div>
    <div class="brand-band"><p class="brand-name">MERIDIAN<span>NEURO LABS</span></p></div>
  </section>

  <!-- Title and Content -->
  <section class="slide slide--wide" style="left:422px;top:148px">
    <div class="emblem" role="img" aria-label="Dot cluster emblem"></div>
    <h2 class="slide-title">Title and Content</h2>
    <ul class="bullets">
      <li>Click to edit Master text styles</li>
      <li class="l2">Second level</li>
      <li class="l3">Third level</li>
      <li class="l4">Fourth level</li>
      <li class="l5">Fifth level</li>
    </ul>
    <div class="footer-band"><p class="footer-name">MERIDIAN<b>NEURO LABS</b></p></div>
  </section>

  <!-- Title Only -->
  <section class="slide" style="left:825px;top:148px">
    <div class="emblem" role="img" aria-label="Dot cluster emblem"></div>
    <h2 class="slide-title">Title Only</h2>
    <div class="footer-band"><p class="footer-name">MERIDIAN<b>NEURO LABS</b></p></div>
  </section>

  <!-- Pie Chart -->
  <section class="slide" style="left:25px;top:437px">
    <div class="emblem" role="img" aria-label="Dot cluster emblem"></div>
    <h2 class="slide-title" style="top:22px">Pie Chart</h2>
    <svg class="chart" viewBox="0 0 332 254">
      <text x="165" y="80" font-size="10" font-weight="700" text-anchor="middle">Chart Title</text>
      <path d="M180 157 L180 105 A52 52 0 1 1 154.95 202.57Z" fill="#2e5f9e" stroke="#fff"/>
      <path d="M180 157 L154.95 202.57 A52 52 0 0 1 131.65 137.86Z" fill="var(--brand-mid)" stroke="#fff"/>
      <path d="M180 157 L131.65 137.86 A52 52 0 0 1 152.14 113.10Z" fill="var(--brand-light)" stroke="#fff"/>
      <path d="M180 157 L152.14 113.10 A52 52 0 0 1 180 105Z" fill="var(--brand-bright)" stroke="#fff"/>
      <g font-size="6.5" fill="#555" text-anchor="middle">
        <text x="230" y="167">1st Qtr</text><text x="230" y="175">58%</text>
        <text x="100" y="170">2nd Qtr</text><text x="100" y="178">23%</text>
        <text x="113" y="110">3rd Qtr</text><text x="113" y="118">10%</text>
        <text x="150" y="94">4th Qtr</text><text x="150" y="102">9%</text>
      </g>
    </svg>
    <div class="footer-band"><p class="footer-name">MERIDIAN<b>NEURO LABS</b></p></div>
  </section>

  <!-- Bar Chart -->
  <section class="slide slide--wide" style="left:422px;top:437px">
    <div class="emblem" role="img" aria-label="Dot cluster emblem"></div>
    <h2 class="slide-title" style="top:20px">Bar Chart</h2>
    <svg class="chart" viewBox="0 0 338 254">
      <g font-size="5" fill="#555" text-anchor="end">
        <text x="60" y="191">0</text><text x="60" y="175">1</text><text x="60" y="159">2</text><text x="60" y="143">3</text>
        <text x="60" y="127">4</text><text x="60" y="111">5</text><text x="60" y="95">6</text><text x="60" y="79">7</text>
      </g>
      <line x1="64" y1="77" x2="64" y2="189" stroke="#bbb" stroke-width=".5"/>
      <line x1="64" y1="189" x2="256" y2="189" stroke="#bbb" stroke-width=".5"/>
      <g fill="#2e5f9e"><rect x="77" y="120.2" width="6" height="68.8"/><rect x="123" y="149" width="6" height="40"/><rect x="169" y="133" width="6" height="56"/><rect x="215" y="117" width="6" height="72"/></g>
      <g fill="var(--brand-light)"><rect x="84" y="150.6" width="6" height="38.4"/><rect x="130" y="118.6" width="6" height="70.4"/><rect x="176" y="160.2" width="6" height="28.8"/><rect x="222" y="144.2" width="6" height="44.8"/></g>
      <g fill="var(--brand-dark)"><rect x="91" y="157" width="6" height="32"/><rect x="137" y="141" width="6" height="48"/><rect x="183" y="93" width="6" height="96"/><rect x="229" y="109" width="6" height="80"/></g>
      <g fill="var(--brand-bright)"><rect x="98" y="109" width="6" height="80"/><rect x="144" y="128.2" width="6" height="60.8"/><rect x="190" y="144.2" width="6" height="44.8"/><rect x="236" y="137.8" width="6" height="51.2"/></g>
      <g font-size="5" text-anchor="middle">
        <text x="80" y="117">4.3</text><text x="87" y="148">2.4</text><text x="94" y="154">2</text><text x="101" y="106">5</text>
        <text x="126" y="146">2.5</text><text x="133" y="116">4.4</text><text x="140" y="138">3</text><text x="147" y="125">3.8</text>
        <text x="172" y="130">3.5</text><text x="179" y="157">1.8</text><text x="186" y="90">6</text><text x="193" y="141">2.8</text>
        <text x="218" y="114">4.5</text><text x="225" y="141">2.8</text><text x="232" y="106">5</text><text x="239" y="135">3.2</text>
        <text x="91" y="199">A</text><text x="137" y="199">B</text><text x="183" y="199">C</text><text x="229" y="199">D</text>
      </g>
      <g font-size="5">
        <circle cx="266" cy="122" r="1.3" fill="#2e5f9e"/><text x="269" y="124">S1</text>
        <circle cx="266" cy="131" r="1.3" fill="var(--brand-light)"/><text x="269" y="133">S2</text>
        <circle cx="266" cy="140" r="1.3" fill="var(--brand-dark)"/><text x="269" y="142">S3</text>
        <circle cx="266" cy="149" r="1.3" fill="var(--brand-bright)"/><text x="269" y="151">S4</text>
      </g>
    </svg>
    <div class="footer-band"><p class="footer-name">MERIDIAN<b>NEURO LABS</b></p></div>
  </section>

  <!-- Line Chart -->
  <section class="slide" style="left:825px;top:433px">
    <div class="emblem" role="img" aria-label="Dot cluster emblem"></div>
    <h2 class="slide-title" style="top:22px">Line Chart</h2>
    <svg class="chart" viewBox="0 0 332 254">
      <g font-size="5" fill="#555" text-anchor="end">
        <text x="33" y="191">0</text><text x="33" y="178">0.5</text><text x="33" y="165">1</text><text x="33" y="152">1.5</text><text x="33" y="139">2</text>
        <text x="33" y="127">2.5</text><text x="33" y="114">3</text><text x="33" y="101">3.5</text><text x="33" y="88">4</text><text x="33" y="75">4.5</text><text x="33" y="62">5</text>
      </g>
      <line x1="37" y1="60" x2="37" y2="189" stroke="#bbb" stroke-width=".5"/>
      <line x1="37" y1="189" x2="235" y2="189" stroke="#bbb" stroke-width=".5"/>
      <polyline points="68,78.1 117,124.5 166,98.7 215,72.9" fill="none" stroke="var(--brand-light)" stroke-width="1.5"/>
      <polyline points="68,127.1 117,75.5 166,142.6 215,116.8" fill="none" stroke="var(--brand-dark)" stroke-width="1.2"/>
      <polyline points="68,163.2 117,158 166,121.9 215,150.3" fill="none" stroke="#3d6aa8" stroke-width="1.2"/>
      <polyline points="68,178.7 117,101.3 166,72.9 215,93.5" fill="none" stroke="var(--brand-mid)" stroke-width="1.5"/>
      <g fill="var(--brand-light)"><circle cx="68" cy="78.1" r="1.6"/><circle cx="117" cy="124.5" r="1.6"/><circle cx="166" cy="98.7" r="1.6"/><circle cx="215" cy="72.9" r="1.6"/></g>
      <g fill="var(--brand-dark)"><circle cx="68" cy="127.1" r="1.6"/><circle cx="117" cy="75.5" r="1.6"/><circle cx="166" cy="142.6" r="1.6"/><circle cx="215" cy="116.8" r="1.6"/></g>
      <g fill="#3d6aa8"><circle cx="68" cy="163.2" r="1.6"/><circle cx="117" cy="158" r="1.6"/><circle cx="166" cy="121.9" r="1.6"/><circle cx="215" cy="150.3" r="1.6"/></g>
      <g fill="var(--brand-mid)"><circle cx="68" cy="178.7" r="1.6"/><circle cx="117" cy="101.3" r="1.6"/><circle cx="166" cy="72.9" r="1.6"/><circle cx="215" cy="93.5" r="1.6"/></g>
      <g font-size="5" text-anchor="middle">
        <text x="68" y="74">4.3</text><text x="117" y="121">2.5</text><text x="166" y="95">3.5</text><text x="215" y="69">4.5</text>
        <text x="68" y="123">2.4</text><text x="117" y="72">4.4</text><text x="166" y="151">1.8</text><text x="215" y="113">2.8</text>
        <text x="68" y="160">1</text><text x="117" y="154">1.2</text><text x="166" y="118">2.6</text><text x="215" y="147">1.5</text>
        <text x="68" y="176">0.4</text><text x="117" y="97" font-weight="700">3.4</text><text x="166" y="69" font-weight="700">4.5</text><text x="215" y="90" font-weight="700">3.7</text>
        <text x="68" y="199">Category 1</text><text x="117" y="199">Category 2</text><text x="166" y="199">Category 3</text><text x="215" y="199">Category 4</text>
      </g>
      <g font-size="4.5">
        <line x1="249" y1="150" x2="255" y2="150" stroke="var(--brand-light)"/><text x="257" y="152">Series 1</text>
        <line x1="249" y1="158" x2="255" y2="158" stroke="var(--brand-dark)"/><text x="257" y="160">Series 2</text>
        <line x1="249" y1="166" x2="255" y2="166" stroke="#3d6aa8"/><text x="257" y="168">Series 3</text>
        <line x1="249" y1="174" x2="255" y2="174" stroke="var(--brand-mid)"/><text x="257" y="176">Series 4</text>
      </g>
    </svg>
    <div class="footer-band"><p class="footer-name">MERIDIAN<b>NEURO LABS</b></p></div>
  </section>

  <!-- Table -->
  <section class="slide" style="left:25px;top:733px">
    <div class="emblem" role="img" aria-label="Dot cluster emblem"></div>
    <h2 class="slide-title" style="top:24px">Table</h2>
    <table class="data-table">
      <thead><tr><th>Title A</th><th>Title B</th><th>Title C</th><th>Title D</th><th>Title E</th></tr></thead>
      <tbody>
        <tr><td>Text here</td><td>1234567890</td><td>1234567890</td><td>1234567890</td><td>1234567890</td></tr>
        <tr><td>Text here</td><td>1234567890</td><td>1234567890</td><td>1234567890</td><td>1234567890</td></tr>
        <tr><td>Text here</td><td>1234567890</td><td>1234567890</td><td>1234567890</td><td>1234567890</td></tr>
        <tr><td>Text here</td><td>1234567890</td><td>1234567890</td><td>1234567890</td><td>1234567890</td></tr>
        <tr><td>Text here</td><td>1234567890</td><td>1234567890</td><td>1234567890</td><td>1234567890</td></tr>
        <tr><td>Text here</td><td>1234567890</td><td>1234567890</td><td>1234567890</td><td>1234567890</td></tr>
        <tr><td>Text here</td><td>1234567890</td><td>1234567890</td><td>1234567890</td><td>1234567890</td></tr>
        <tr><td>Text here</td><td>1234567890</td><td>1234567890</td><td>1234567890</td><td>1234567890</td></tr>
      </tbody>
    </table>
    <div class="footer-band"><p class="footer-name">MERIDIAN<b>NEURO LABS</b></p></div>
  </section>

  <!-- Blank -->
  <section class="slide slide--wide" style="left:422px;top:733px">
    <div class="emblem" role="img" aria-label="Dot cluster emblem"></div>
    <p class="blank-label">BLANK</p>
    <div class="footer-band"><p class="footer-name">MERIDIAN<b>NEURO LABS</b></p></div>
  </section>

  <!-- Close -->
  <section class="slide" style="left:816px;top:733px;width:339px">
    <div class="hero-band" role="img" aria-label="Banner with rows of light blue dots on a blue gradient"></div>
    <h2 class="cover-title">Thank You</h2>
    <p class="cover-date">October 26, 2013</p>
    <div class="rule" style="top:168px"></div>
    <div class="brand-band"><p class="brand-name">MERIDIAN<span>NEURO LABS</span></p></div>
  </section>
</div>
</body>
</html>
```